PowerPoint Template Needed for Investment Firm

Meridale Capital Management is an emerging wealth management firm based in New Jersey. It offers superior investment returns to high net worth individuals and institutions by finding undervalued assets.

We recently selected a company logo which was inspired by the Meridale constellation. Beta Tucanae is a group of six stars, containing star cluster 47 Tucanae, rated the second brightest object in the sky.

Now we need a PowerPoint template with the designs for the following:

1. Title/cover page slide
2. Content slide with title
3. Section slide - to introduce a new section
4. Final slide - with contact information

The slides will be used at investor presentations, that is, to provide information about the company to potential investors. Since we are an investment firm, the design should project a sense of stability, growth and professionalism. The owner is interested in something simple yet striking, which of course is consistent with the logo. I'm thinking more conservative colors and Sans Serif fonts.

I plan on changing the status to non-refundable once I see some designs that I really like.

Target Market(s)

Wealthy individuals, probably middle aged or older, in the US

Industry/Entity Type

Conservative

Requirements
Must have
• Sans serif fonts
Clean, very professional look
Conservative colors that complement existing logo
Should not have
• Anything too busy or complicated

```html
<!DOCTYPE html>
<html lang="en">
<head>
<meta charset="utf-8">
<title>Meridale Capital Management – Slide Template</title>
<link href="https://fonts.googleapis.com/css2?family=PT+Sans:wght@400;700&display=swap" rel="stylesheet">
<style>
:root{
  --navy:#0b1a6b;
  --royal:#1a3fb8;
  --bright:#2f6fd6;
  --sky:#5b8fd6;
  --pale:#9ec0ee;
  --text-gray:#7a7a7a;
  --dark-gray:#555;
  --row-a:#c9cce6;
  --row-b:#e3e4f2;
  --frame:#9a9a9a;
}
*{margin:0;padding:0;box-sizing:border-box}
html,body{width:1200px;height:1000px;overflow:hidden;background:#fff}
body{font-family:"PT Sans",sans-serif;position:relative}
.slide{position:absolute;width:377px;height:285px;background:#fff;border:1px solid var(--frame);box-shadow:3px 3px 4px rgba(0,0,0,.35);overflow:hidden}
.ticker-photo{position:absolute;left:0;top:0;width:100%;
  background:
   radial-gradient(ellipse 60% 40% at 45% 40%,rgba(90,150,255,.55),transparent 70%),
   radial-gradient(ellipse 50% 30% at 80% 20%,rgba(70,130,255,.4),transparent 70%),
   linear-gradient(180deg,#0a1660 0%,#1434b0 45%,#0d2290 75%,#08145a 100%)}
.photo-rule{position:absolute;left:0;width:100%;height:8px;background:linear-gradient(90deg,#6a6a6a,#9a9a9a 50%,#6a6a6a)}
.brand-name{position:absolute;right:10px;bottom:14px;font-size:9px;font-weight:400;color:var(--navy);white-space:nowrap}
.header{position:absolute;left:0;top:0;width:377px;height:46px}
.header-title{position:absolute;left:12px;top:7px;color:#fff;font-size:18px}
.header-brand{position:absolute;right:6px;top:16px;font-size:7.5px;font-weight:400;color:var(--navy);white-space:nowrap}
.footer{position:absolute;left:0;bottom:0;width:100%;height:8px;background:linear-gradient(90deg,#8a8a8a,#555);color:#fff;font-size:5px;line-height:8px;padding:0 10px;display:flex;justify-content:space-between}
.bullets{list-style:none;font-size:11.5px;line-height:13.5px;color:var(--text-gray)}
.bullets>li{position:relative;padding-left:14px;margin-bottom:2px}
.bullets>li::before{content:"•";position:absolute;left:2px;color:var(--royal)}
.bullets .lead{color:var(--royal)}
.bullets ul{list-style:none;margin:3px 0 0 4px}
.bullets ul li{position:relative;padding-left:18px;font-size:10.5px;margin-bottom:4px}
.bullets ul li::before{content:"–";position:absolute;left:2px;color:var(--royal)}
.block-title{position:absolute;left:0;width:100%;text-align:center;color:var(--bright);font-size:15px;font-weight:700}
.block-desc{position:absolute;left:0;width:100%;text-align:center;color:var(--dark-gray);font-size:9px}
.data-table{position:absolute;left:62px;top:113px;width:252px;border-collapse:collapse;font-size:9px;text-align:center}
.data-table th{background:var(--bright);color:#fff;font-weight:700;height:15px;border-right:1px solid #fff}
.data-table td{height:15px;color:#333;border-right:1px solid #fff}
.data-table tr:nth-child(odd) td{background:var(--row-a)}
.data-table tr:nth-child(even) td{background:var(--row-b)}
.photo-box{position:absolute;border-radius:10px;background:linear-gradient(160deg,#eef1f6,#c8d2e0 60%,#9fb0c8)}
.dotted{position:absolute;border:1px dashed #6a8ed0}
.dash-list{list-style:none;font-size:7px;line-height:10px;color:var(--text-gray);padding:8px 8px 0 12px}
.dash-list li{position:relative;padding-left:14px;margin-bottom:5px}
.dash-list li::before{content:"–";position:absolute;left:0;color:var(--royal)}
.big-caption{position:absolute;left:0;width:100%;text-align:center;color:#fff;font-weight:700;letter-spacing:.01em}
.contact{position:absolute;left:30px;top:240px;font-size:7.5px;line-height:10px;color:var(--text-gray)}
.contact b{color:var(--royal);font-weight:400;display:inline-block;width:34px;text-align:right;margin-right:3px}
</style>
</head>
<body>

<!-- Cover -->
<section class="slide" style="left:15px;top:50px">
  <div class="ticker-photo" style="height:222px" role="img" aria-label="Blue stock market ticker board with prices and arrows"></div>
  <div class="photo-rule" style="top:222px"></div>
  <div style="position:absolute;left:0;top:155px;width:293px;height:23px;background:#fff;padding-left:10px;color:var(--royal);font-size:16px;line-height:23px">PRESENTATION TITLE</div>
  <div style="position:absolute;left:10px;top:238px;font-size:11px;color:var(--text-gray)">Presentation subtitle and / or speaker</div>
  <div class="brand-name">Meridale Capital Management</div>
</section>

<!-- Text-only -->
<section class="slide" style="left:411px;top:50px">
  <svg class="header" viewBox="0 0 377 46"><defs><linearGradient id="hg1" x1="0" x2="1"><stop offset="0" stop-color="#1a3fb8"/><stop offset="1" stop-color="#0b1a6b"/></linearGradient></defs><polygon points="0,0 340,0 325,38 0,38" fill="url(#hg1)"/><polygon points="0,38 325,38 322,44 0,44" fill="#8a8a8a"/></svg>
  <div class="header-title">Text-only slide</div>
  <div class="header-brand">Meridale</div>
  <ul class="bullets" style="position:absolute;left:10px;top:45px;width:360px">
    <li><span class="lead">In sed dictum augue.</span> In eu urna nec massa vehicula porttitor.</li>
    <li><span class="lead">Phasellus elementum lacus vel elit malesuada porta.</span> In pretium ullamcorper leo, in imperdiet nunc suscipit at.</li>
    <li><span class="lead">Vestibulum eget pretium magna.</span> Suspendisse potenti. Quisque vulputate nunc vitae ante sagittis vehicula.</li>
    <li><span class="lead">Donec et libero eget purus ultrices mattis.</span> Suspendisse ut sapien et tellus fermentum laoreet.
      <ul>
        <li>Morbi vitae nibh non dui molestie egestas nec eu velit.</li>
        <li>Vivamus vel quam id est fringilla tincidunt. Nullam vitae sodales nisi.</li>
        <li>Donec eu dolor lectus. Nulla orci sapien, consequat non faucibus aliquam vel diam.</li>
      </ul></li>
    <li><span class="lead">Maecenas in tincidunt purus.</span> Ut non aliquet mauris. In sapien sapien, suscipit varius vestibulum ac, pharetra in magna.</li>
  </ul>
  <div class="footer"><span>19-03-2013</span><span>2</span></div>
</section>

<!-- Text and image -->
<section class="slide" style="left:810px;top:50px">
  <svg class="header" viewBox="0 0 377 46"><polygon points="0,0 340,0 325,38 0,38" fill="url(#hg1)"/><polygon points="0,38 325,38 322,44 0,44" fill="#8a8a8a"/></svg>
  <div class="header-title">Text and image slide</div>
  <div class="header-brand">Meridale</div>
  <ul class="bullets" style="position:absolute;left:10px;top:45px;width:200px;font-size:11px;line-height:13px">
    <li><span class="lead">In sed dictum augue.</span> In eu urna nec massa vehicula porttitor.</li>
    <li><span class="lead">Donec et libero eget purus ultrices mattis.</span></li>
    <li><span class="lead">Suspendisse ut sapien et tellus.</span>Ut non aliquet mauris.
      <ul>
        <li>Morbi vitae nibh non dui molestie egestas nec eu velit.</li>
        <li>Vivamus vel quam id est fringilla tincidunt. Nullam vitae sodales nisi.</li>
      </ul></li>
    <li><span class="lead">Maecenas in tincidunt purus.</span> Ut non aliquet mauris.</li>
    <li><span class="lead">In sapien sapien, suscipit varius.</span> Vestibulum ac, pharetra in magna.</li>
  </ul>
  <div class="photo-box" style="left:210px;top:57px;width:145px;height:120px" role="img" aria-label="Calculator, pen and financial charts on a desk"></div>
  <div class="footer"><span>19-03-2013</span><span>3</span></div>
</section>

<!-- Section -->
<section class="slide" style="left:15px;top:363px">
  <div class="ticker-photo" style="height:222px" role="img" aria-label="Blue stock market ticker board with prices and arrows"></div>
  <div class="photo-rule" style="top:222px"></div>
  <div class="big-caption" style="top:124px;font-size:25px">FINANCIAL RETURNS</div>
  <div class="brand-name">Meridale Capital Management</div>
</section>

<!-- Table -->
<section class="slide" style="left:415px;top:363px">
  <svg class="header" viewBox="0 0 377 46"><polygon points="0,0 340,0 325,38 0,38" fill="url(#hg1)"/><polygon points="0,38 325,38 322,44 0,44" fill="#8a8a8a"/></svg>
  <div class="header-title">Table slide</div>
  <div class="header-brand">Meridale</div>
  <div class="block-title" style="top:57px">Table title</div>
  <div class="block-desc" style="top:79px">Small description of the table contents and its conclusions</div>
  <table class="data-table">
    <thead><tr><th>Category A</th><th>Category B</th><th>Category C</th><th>Category D</th></tr></thead>
    <tbody>
      <tr><td>111.333</td><td>111.555</td><td>111.333</td><td>111.555</td></tr>
      <tr><td>444.555</td><td>444.333</td><td>444.555</td><td>444.333</td></tr>
      <tr><td>111.222</td><td>222.333</td><td>111.222</td><td>222.333</td></tr>
      <tr><td>222.555</td><td>555.333</td><td>222.555</td><td>555.333</td></tr>
      <tr><td>333.444</td><td>333.111</td><td>333.444</td><td>333.111</td></tr>
    </tbody>
  </table>
  <div class="footer"><span>19-03-2013</span><span>5</span></div>
</section>

<!-- Pie chart -->
<section class="slide" style="left:810px;top:363px">
  <svg class="header" viewBox="0 0 377 46"><polygon points="0,0 340,0 325,38 0,38" fill="url(#hg1)"/><polygon points="0,38 325,38 322,44 0,44" fill="#8a8a8a"/></svg>
  <div class="header-title">Pie chart slide</div>
  <div class="header-brand">Meridale</div>
  <div class="block-title" style="top:57px">Chart title</div>
  <div class="block-desc" style="top:79px">Small description of the chart categories and its conclusions</div>
  <svg style="position:absolute;left:123px;top:106px" width="130" height="130" viewBox="0 0 130 130">
    <g transform="rotate(-90 65 65)" fill="none" stroke-width="32">
      <circle cx="65" cy="65" r="48" stroke="#0b1a6b" stroke-dasharray="138.7 301.6"/>
      <circle cx="65" cy="65" r="48" stroke="#5b8fd6" stroke-dasharray="72.4 301.6" stroke-dashoffset="-138.7"/>
      <circle cx="65" cy="65" r="48" stroke="#2f6fd6" stroke-dasharray="54.3 301.6" stroke-dashoffset="-211.1"/>
      <circle cx="65" cy="65" r="48" stroke="#1a3ab0" stroke-dasharray="36.2 301.6" stroke-dashoffset="-265.4"/>
    </g>
  </svg>
  <svg style="position:absolute;left:108px;top:238px" width="170" height="12" font-family="PT Sans, sans-serif" font-size="8" fill="#7a7a7a">
    <rect x="2" y="3" width="5" height="5" fill="#0b1a6b"/><text x="9" y="8">1st Qtr</text>
    <rect x="42" y="3" width="5" height="5" fill="#5b8fd6"/><text x="49" y="8">2nd Qtr</text>
    <rect x="84" y="3" width="5" height="5" fill="#2f6fd6"/><text x="91" y="8">3rd Qtr</text>
    <rect x="125" y="3" width="5" height="5" fill="#1a3ab0"/><text x="132" y="8">4th Qtr</text>
  </svg>
  <div class="footer"><span>19-03-2013</span><span>6</span></div>
</section>

<!-- Charts -->
<section class="slide" style="left:12px;top:689px">
  <svg class="header" viewBox="0 0 377 46"><polygon points="0,0 340,0 325,38 0,38" fill="url(#hg1)"/><polygon points="0,38 325,38 322,44 0,44" fill="#8a8a8a"/></svg>
  <div class="header-title">Charts slide</div>
  <div class="header-brand">Meridale</div>
  <div class="dotted" style="left:14px;top:41px;width:178px;height:101px">
    <svg width="176" height="99" viewBox="0 0 176 99" font-family="PT Sans, sans-serif" font-size="6" fill="#333">
      <g stroke="#999" stroke-width=".6"><line x1="18" y1="8" x2="18" y2="82"/><line x1="18" y1="82" x2="125" y2="82"/></g>
      <text x="10" y="84">0</text><text x="10" y="72">1</text><text x="10" y="60">2</text><text x="10" y="47">3</text><text x="10" y="35">4</text><text x="10" y="22">5</text><text x="10" y="10">6</text>
      <text x="22" y="92">2010</text><text x="49" y="92">2011</text><text x="76" y="92">2012</text><text x="103" y="92">2013</text>
      <polyline points="28,30 55,52 82,40 109,27" fill="none" stroke="#0b1a6b" stroke-width="1.2"/>
      <polyline points="28,53 55,29 82,60 109,48" fill="none" stroke="#2f6fd6" stroke-width="1.2"/>
      <polyline points="28,58 55,58 82,46 109,21" fill="none" stroke="#9ec0ee" stroke-width="1.2"/>
      <g fill="#0b1a6b"><circle cx="28" cy="30" r="1.6"/><circle cx="55" cy="52" r="1.6"/><circle cx="82" cy="40" r="1.6"/><circle cx="109" cy="27" r="1.6"/></g>
      <g fill="#2f6fd6"><rect x="26.5" y="51.5" width="3" height="3"/><rect x="53.5" y="27.5" width="3" height="3"/><rect x="80.5" y="58.5" width="3" height="3"/><rect x="107.5" y="46.5" width="3" height="3"/></g>
      <line x1="135" y1="36" x2="145" y2="36" stroke="#0b1a6b"/><text x="148" y="38">A</text>
      <line x1="135" y1="46" x2="145" y2="46" stroke="#2f6fd6"/><text x="148" y="48">B</text>
      <line x1="135" y1="56" x2="145" y2="56" stroke="#9ec0ee"/><text x="148" y="58">C</text>
    </svg>
  </div>
  <div class="dotted" style="left:14px;top:148px;width:178px;height:88px">
    <svg width="176" height="86" viewBox="0 0 176 86" font-family="PT Sans, sans-serif" font-size="6" fill="#333">
      <line x1="24" y1="4" x2="24" y2="72" stroke="#999" stroke-width=".6"/>
      <line x1="24" y1="72" x2="120" y2="72" stroke="#999" stroke-width=".6"/>
      <text x="4" y="13">2013</text><text x="4" y="30">2012</text><text x="4" y="47">2011</text><text x="4" y="64">2010</text>
      <text x="22" y="80">0</text><text x="53" y="80">2</text><text x="85" y="80">4</text><text x="117" y="80">6</text>
      <rect x="24" y="5" width="80" height="3.5" fill="#9ec0ee"/><rect x="24" y="9" width="45" height="3.5" fill="#2f6fd6"/><rect x="24" y="13" width="72" height="3.5" fill="#0b1a6b"/>
      <rect x="24" y="22" width="48" height="3.5" fill="#9ec0ee"/><rect x="24" y="26" width="29" height="3.5" fill="#2f6fd6"/><rect x="24" y="30" width="56" height="3.5" fill="#0b1a6b"/>
      <rect x="24" y="39" width="32" height="3.5" fill="#9ec0ee"/><rect x="24" y="43" width="70" height="3.5" fill="#2f6fd6"/><rect x="24" y="47" width="40" height="3.5" fill="#0b1a6b"/>
      <rect x="24" y="56" width="32" height="3.5" fill="#9ec0ee"/><rect x="24" y="60" width="38" height="3.5" fill="#2f6fd6"/><rect x="24" y="64" width="69" height="3.5" fill="#0b1a6b"/>
      <rect x="132" y="24" width="4" height="4" fill="#9ec0ee"/><text x="139" y="28">C</text>
      <rect x="132" y="34" width="4" height="4" fill="#2f6fd6"/><text x="139" y="38">B</text>
      <rect x="132" y="44" width="4" height="4" fill="#0b1a6b"/><text x="139" y="48">A</text>
    </svg>
  </div>
  <div class="dotted" style="left:197px;top:41px;width:164px;height:195px">
    <ul class="dash-list">
      <li>Lorem ipsum dolor sit amet, consectetur adipiscing elit. Proin in velit facilisis libero consectetur adipiscing.</li>
      <li>Aenean congue euismod erat, eu adipiscing dui gravida in.</li>
      <li>Donec vehicula tellus sit amet est aliquam ac pretium lacus aliquam.</li>
      <li>Suspendisse potenti. Integer est nunc, dignissim ac sagittis sit amet, pretium sit amet libero.</li>
      <li>Cras id nibh et ipsum ultrices pretium. Curabitur id leo tellus, a convallis justo. In turpis magna, aliquam ut consequat et, tempor ultrices mauris.</li>
    </ul>
  </div>
  <div class="footer"><span>19-03-2013</span><span>7</span></div>
</section>

<!-- Closing -->
<section class="slide" style="left:410px;top:689px">
  <div class="ticker-photo" style="height:217px" role="img" aria-label="Blue stock market ticker board with prices and arrows"></div>
  <div class="photo-rule" style="top:217px"></div>
  <div class="big-caption" style="top:128px;font-size:25px">THANK YOU!</div>
  <div class="contact">
    <div><b>Address:</b>48 Harbor Ave. Newark, NJ 07102</div>
    <div><b>Website:</b>www.meridalecapmgmt.com</div>
    <div><b>E-mail:</b>jharlow@meridalecapmgmt.com</div>
  </div>
  <div class="brand-name">Meridale Capital Management</div>
</section>

</body>
</html>
```